Grins of Maplecrest - Dental, needs a redesign

Purpose:
Redesign website: http://www.grinsofmaplecrest.example/

Sections are important, but for content, we can use existing website or have some placeholder text to fill in later.

Some of the required sections:
About us, contact us, services, our offices, our staff, patient education, patient forms (link to Molvaro can be used here), link to friendwall, testimonials

Editability:
We would like to be able to update and edit the content in the future, for small changes

Pictures:
Here is a link to the staff pictures we’d like to use on the website:
https://www.filecrate.example/sh/503k7pq2vv884x9/BBDPyrTe_wKQj7ZumfXKTgghb?dl=0
You don't have to use all the pictures; just a few.

Friendwall page:
https://www.friendwall.example/Grins-of-Maplecrest-527163048915276

Colors: Calming colors/images for a soothing feeling... to assure the patient that it'll not be that bad.

Target Market(s)

General population

Industry/Entity Type

Dental Clinic

Coding

Coded - Design and coding required

Number of Pages Required

5+ page

Requirements
Must have
• About us, contact us, services, our offices, our staff, patient education, patient forms (link to Molvaro can be used here), link to friendwall, testimonials.
• Just create the placeholders for content or use from existing website.
• The staff picture of everyone needs to be on the home page - because that makes it more personal and has received positive feedback from many patients.

```html
<!DOCTYPE html>
<html lang="en">
<head>
<meta charset="utf-8">
<title>Grins of Maplecrest - Dental</title>
<link href="https://fonts.googleapis.com/css2?family=Raleway:wght@300;400;500;600;700&family=Kaushan+Script&display=swap" rel="stylesheet">
<style>
:root{
  --teal:#37c3d4;
  --purple:#b48ad9;
  --pink:#e8179b;
  --ink:#333740;
  --muted:#6b6f78;
  --link:#2e9fd0;
  --line:#d4d6da;
  --panel:#eef1f4;
  --footer:#232427;
  --white:#ffffff;
}
*{box-sizing:border-box;margin:0;padding:0}
html,body{width:1200px;height:4235px;overflow:hidden}
body{font-family:'Raleway',sans-serif;color:var(--ink);background:var(--white);position:relative}
.abs{position:absolute}

/* header */
.site-header{position:absolute;top:0;left:0;width:1200px;height:113px;background:var(--white)}
.brand{position:absolute;left:82px;top:24px;display:flex;align-items:center;gap:14px}
.brand-mark{width:54px;height:54px;border-radius:50%;background:var(--purple)}
.brand-name{font-size:24px;font-weight:600;color:#3a4a86;line-height:1.2}
.main-nav{position:absolute;right:82px;top:44px;display:flex;gap:22px;font-size:17px}
.main-nav a{color:#5a5f68;text-decoration:none}
.main-nav a.active{color:var(--teal)}
.rule-band{position:absolute;left:0;width:1200px;height:4px;background:linear-gradient(90deg,var(--purple),var(--teal))}

/* hero */
.hero{position:absolute;top:113px;left:0;width:1200px;height:559px;background:linear-gradient(100deg,#eef0fb 0%,#e4e9f5 40%,#c9b7a6 70%,#8e8a92 100%)}
.hero-tagline{position:absolute;left:80px;top:190px;font-family:'Kaushan Script',cursive}
.hero-tagline .line1{font-size:58px;color:#151515;display:block}
.hero-tagline .line2{font-size:66px;color:var(--pink);display:block;margin-top:4px}

/* section heading */
.section-title{position:absolute;left:0;width:1200px;text-align:center;font-size:36px;font-weight:400;color:#2f3238}
.title-divider{position:absolute;left:395px;width:410px;height:20px}
.title-divider::before,.title-divider::after{content:"";position:absolute;top:9px;width:180px;height:3px;background:var(--line)}
.title-divider::before{left:0}
.title-divider::after{right:0}
.title-divider svg{position:absolute;left:195px;top:0}

/* intro */
.intro-copy{position:absolute;left:80px;width:1040px;top:820px;text-align:center;font-size:13.5px;line-height:1.55;color:var(--muted)}
.intro-copy p{margin-bottom:16px}
.intro-photo{position:absolute;left:0;top:975px;width:1200px;height:211px;background:linear-gradient(180deg,#ffffff 0%,#f2e8f6 60%,#e7dcef 100%)}

/* services */
.services-grid{position:absolute;left:80px;top:1356px;width:1040px;display:grid;grid-template-columns:repeat(4,1fr);column-gap:30px;row-gap:38px}
.service{text-align:center}
.service-icon{width:112px;height:112px;border:2px solid #555a63;border-radius:50%;margin:0 auto;display:flex;align-items:center;justify-content:center}
.service h3{font-size:21px;font-weight:500;margin-top:20px;color:#2f3238}
.service p{font-size:12.5px;line-height:1.5;color:var(--muted);margin-top:10px;padding:0 16px}

/* gallery */
.gallery-tile{position:absolute;height:226px}

/* team */
.team-card{position:absolute;top:2838px;width:225px;height:246px;border:1px solid var(--line);padding:6px;background:var(--white)}
.team-photo{width:100%;height:100%;background:linear-gradient(180deg,#f4f4f4 0%,#d9d9d9 55%,#2d2d33 100%);position:relative}
.team-caption{position:absolute;left:0;bottom:8px;width:100%;text-align:center}
.team-caption .name{display:block;font-size:15px;color:var(--white);font-weight:500}
.team-caption .role{display:block;font-size:12px;color:var(--purple)}
.slider-arrow{position:absolute;top:2945px}

/* testimonials */
.testimonial{position:absolute;top:3290px;width:503px;height:141px;border:2px solid #45484f;background:var(--white);padding:22px 90px 0 30px;font-size:12.5px;line-height:1.5;color:var(--muted)}
.testimonial .quote-mark{position:absolute;left:10px;top:-8px;font-size:70px;color:#dfe3ea;font-family:Georgia,serif}
.testimonial p{position:relative}
.testimonial .author{display:block;margin-top:10px;font-size:11px;color:var(--link);position:relative}
.testimonial .author small{display:block;color:var(--muted);font-size:10.5px}
.avatar{position:absolute;right:-22px;bottom:-36px;width:104px;height:104px;border-radius:50%;border:3px solid #c8202e;background:linear-gradient(160deg,#f1e6de,#b89b88)}

/* contact */
.contact{position:absolute;top:3530px;left:0;width:1200px;height:644px;background:var(--panel)}
.contact-info{position:absolute;left:79px;top:3694px;font-size:14px;line-height:1.45;color:#3a3d44}
.contact-info .label{font-size:13px;margin-top:14px;display:block}
.contact-info .label:first-child{margin-top:0}
.contact-info .phone{font-size:29px;color:var(--teal);display:block;margin-top:2px}
.contact-info .hi{color:var(--teal);font-size:17px;display:block}
.hours{font-size:13.5px;margin-top:4px}
.hours span{color:var(--purple)}
.form-divider{position:absolute;left:579px;top:3694px;width:1px;height:420px;background:#c9ccd2}
.contact-form label{position:absolute;left:613px;font-size:14px;color:#3a3d44}
.contact-form .field{position:absolute;left:700px;width:421px;height:42px;border:1px solid #bfc3c9;background:var(--white);font-size:13px;color:#a5a9b0;padding:12px 14px}
.send-btn{position:absolute;left:700px;top:4061px;width:147px;height:46px;background:var(--teal);color:var(--white);font-size:18px;display:flex;align-items:center;justify-content:center}

/* footer */
.site-footer{position:absolute;top:4174px;left:0;width:1200px;height:61px;background:var(--footer);color:#c9ccd2;font-size:12.5px}
.footer-nav{position:absolute;left:79px;top:14px;display:flex;gap:10px}
.footer-nav span.sep{color:#777}
.copyright{position:absolute;left:79px;top:36px;font-size:10.5px;color:#9a9ea6}
.legal{position:absolute;right:130px;top:20px;display:flex;gap:18px}
.social-square{position:absolute;right:79px;top:16px;width:26px;height:26px;background:#3b5aa0}
</style>
</head>
<body>

<header class="site-header">
  <div class="brand">
    <div class="brand-mark"></div>
    <div class="brand-name">Dr. Meera Kalwani, DDS<br>Grins of Maplecrest</div>
  </div>
  <nav class="main-nav">
    <a class="active">Home</a><a>About</a><a>Services</a><a>Patient Education</a><a>Patient Form</a><a>Testimonial</a><a>Contact</a>
  </nav>
</header>
<div class="rule-band" style="top:110px"></div>

<section class="hero" role="img" aria-label="Dentist in a white coat talking with a patient in the treatment chair">
  <div class="hero-tagline">
    <span class="line1">Live The Life With</span>
    <span class="line2">Great Smile</span>
  </div>
</section>
<div class="rule-band" style="top:670px;background:var(--teal);height:3px"></div>

<!-- intro -->
<h2 class="section-title" style="top:712px">Honestly Caring &amp; Quality Dentistry</h2>
<div class="title-divider" style="top:765px"><svg width="20" height="20" viewBox="0 0 20 20"><path d="M4 3h12v8c0 4-3 6-6 7-3-1-6-3-6-7z" fill="none" stroke="var(--teal)" stroke-width="2"/><path d="M7 7h6v3c0 2-1.5 3-3 3.5C8.5 13 7 12 7 10z" fill="var(--purple)"/></svg></div>
<div class="intro-copy">
  <p>Dr. Meera Kalwani provides a full range of dental services to the whole family. Many of our patient families span multiple generations. Our Team are dedicated to taking the time needed to provide the very best care every patient deserves.</p>
  <p>Please tour our web site to learn more about family dentistry, cosmetic dentistry and our restorative dental services. We invite you to call us with any questions you may have – we look forward to meeting you and your family!</p>
  <p>New patients looking for quality dental care in a relaxed environment are welcome! We accept PPO, Indemnity and Traditional insurance plans.</p>
</div>
<div class="intro-photo" role="img" aria-label="Group of smiling friends showing healthy teeth"></div>
<div class="rule-band" style="top:1190px;height:2px;background:linear-gradient(90deg,var(--teal),var(--purple))"></div>

<!-- services -->
<h2 class="section-title" style="top:1234px">Our Dental Services</h2>
<div class="title-divider" style="top:1287px"><svg width="20" height="20" viewBox="0 0 20 20"><path d="M4 3h12v8c0 4-3 6-6 7-3-1-6-3-6-7z" fill="none" stroke="var(--teal)" stroke-width="2"/><path d="M7 7h6v3c0 2-1.5 3-3 3.5C8.5 13 7 12 7 10z" fill="var(--purple)"/></svg></div>
<div class="services-grid">
  <div class="service"><div class="service-icon"><svg width="60" height="60" viewBox="0 0 60 60"><path d="M14 14c6-6 12-2 16-2s10-4 16 2c5 6 2 16 0 22-2 8-3 16-7 16-4 0-4-12-9-12s-5 12-9 12c-4 0-5-8-7-16-2-6-5-16 0-22z" fill="none" stroke="var(--teal)" stroke-width="3"/><circle cx="30" cy="26" r="5" fill="var(--pink)"/></svg></div><h3>Fillings</h3><p>Fillings are done to remove decay and replace the affected tooth structure. It is called a filling because new material fills the hole left.</p></div>
  <div class="service"><div class="service-icon"><svg width="60" height="60" viewBox="0 0 60 60"><path d="M16 10h28c3 0 4 6 0 10H16c-4-4-3-10 0-10z" fill="none" stroke="var(--purple)" stroke-width="3"/><path d="M24 22v28M36 22v28M22 30h16M22 38h16M22 46h16" stroke="var(--teal)" stroke-width="3"/></svg></div><h3>Gum Treatments</h3><p>The gums, ligaments, and bone around the teeth form the foundation for ones teeth. All structures are also referred to as the periodontium.</p></div>
  <div class="service"><div class="service-icon"><svg width="70" height="40" viewBox="0 0 70 40"><path d="M4 8c20 10 42 10 62 0-6 18-18 26-31 26S10 26 4 8z" fill="none" stroke="var(--teal)" stroke-width="3"/><path d="M14 14v8M24 16v10M35 17v11M46 16v10M56 14v8" stroke="var(--teal)" stroke-width="2"/></svg></div><h3>Cosmetic Dentistry</h3><p>This can be anything done to correct imperfections in the appearance of the mouth. Anyone who is unhappy with their smile can have it fixed.</p></div>
  <div class="service"><div class="service-icon"><svg width="60" height="60" viewBox="0 0 60 60"><rect x="12" y="12" width="36" height="36" rx="6" fill="none" stroke="var(--purple)" stroke-width="3"/><path d="M20 22c4-3 8 0 10 0s6-3 10 0c2 4 0 10-2 16-1 4-3 4-4 0-1-3-2-5-4-5s-3 2-4 5c-1 4-3 4-4 0-2-6-4-12-2-16z" fill="var(--teal)"/></svg></div><h3>Root Canal Treatment</h3><p>Root canal treatment (endodontic therapy) is made necessary when a cavity is allowed, through neglect, to reach all the way to the pulp.</p></div>
  <div class="service"><div class="service-icon"><svg width="70" height="50" viewBox="0 0 70 50"><path d="M6 10c5-4 9 0 12 0s7-4 12 0c3 6 0 14-2 22-1 6-3 6-4 0-1-4-3-6-6-6s-5 2-6 6c-1 6-3 6-4 0C6 24 3 16 6 10z" fill="none" stroke="var(--teal)" stroke-width="3"/><path d="M38 10c5-4 9 0 12 0s7-4 12 0c3 6 0 14-2 22-1 6-3 6-4 0-1-4-3-6-6-6s-5 2-6 6c-1 6-3 6-4 0-2-8-5-16-2-22z" fill="none" stroke="var(--teal)" stroke-width="3"/></svg></div><h3>Bonding</h3><p>Bonding involves adhering composite resin material that is matched to the color of the tooth, to the front of the tooth.</p></div>
  <div class="service"><div class="service-icon"><svg width="60" height="50" viewBox="0 0 60 50"><path d="M6 10h48v8c-6 8-42 8-48 0z" fill="none" stroke="#555a63" stroke-width="3"/><path d="M6 32c6-8 42-8 48 0v8H6z" fill="none" stroke="#555a63" stroke-width="3"/><path d="M14 14v6M24 14v7M36 14v7M46 14v6" stroke="var(--teal)" stroke-width="2"/></svg></div><h3>Clear Aligners</h3><p>Clear aligners straighten your teeth with a series of clear virtually invisible custom-molded trays.</p></div>
  <div class="service"><div class="service-icon"><svg width="60" height="60" viewBox="0 0 60 60"><path d="M16 10c5-4 10 0 14 0s9-4 14 0c3 6 1 12-2 16H18c-3-4-5-10-2-16z" fill="none" stroke="var(--teal)" stroke-width="3"/><path d="M24 30h12M25 36h10M26 42h8M28 48h4" stroke="#555a63" stroke-width="3"/></svg></div><h3>Implants</h3><p>A dental implant is an option to replace a missing tooth. In this procedure, a small titanium shaft is surgically implanted into the bone and allowed to set.</p></div>
  <div class="service"><div class="service-icon"><svg width="60" height="60" viewBox="0 0 60 60"><path d="M16 8l6 6 8-6 8 6 6-6v10H16z" fill="var(--purple)"/><path d="M16 20c5-3 10 0 14 0s9-3 14 0c3 6 0 14-2 20-1 8-4 8-5 0-1-4-3-6-7-6s-6 2-7 6c-1 8-4 8-5 0-2-6-5-14-2-20z" fill="none" stroke="var(--teal)" stroke-width="3"/></svg></div><h3>Crowns</h3><p>Crowns are full coverage restorations that are used to cover a tooth that is likely to break, or is too broken down to be restored with a filling.</p></div>
</div>
<div class="rule-band" style="top:1941px;height:2px;background:linear-gradient(90deg,var(--teal),var(--purple))"></div>

<!-- gallery -->
<h2 class="section-title" style="top:1986px">Our Gallery</h2>
<div class="title-divider" style="top:2039px"><svg width="20" height="20" viewBox="0 0 20 20"><path d="M4 3h12v8c0 4-3 6-6 7-3-1-6-3-6-7z" fill="none" stroke="var(--teal)" stroke-width="2"/><path d="M7 7h6v3c0 2-1.5 3-3 3.5C8.5 13 7 12 7 10z" fill="var(--purple)"/></svg></div>
<div class="gallery-tile" style="left:79px;top:2107px;width:345px;background:linear-gradient(135deg,#d8d2c6,#8f8a80)" role="img" aria-label="Staff member beside a treatment room monitor"></div>
<div class="gallery-tile" style="left:429px;top:2107px;width:339px;background:linear-gradient(135deg,#6b4f3e,#2f2a2a)" role="img" aria-label="Staff member at the front desk with patient brochures"></div>
<div class="gallery-tile" style="left:776px;top:2107px;width:342px;background:linear-gradient(180deg,#cfe0ef 0%,#a25a3e 55%,#6e8a4a 100%)" role="img" aria-label="Brick exterior of the dental office"></div>
<div class="gallery-tile" style="left:79px;top:2338px;width:345px;background:linear-gradient(135deg,#f1eeea,#a7b7a8)" role="img" aria-label="Treatment room with dental chair"></div>
<div class="gallery-tile" style="left:429px;top:2338px;width:339px;background:linear-gradient(135deg,#c9a47c,#5b4634)" role="img" aria-label="Waiting room with sofa and chairs"></div>
<div class="gallery-tile" style="left:776px;top:2338px;width:342px;background:linear-gradient(135deg,#2e7a54,#1d5a3d)" role="img" aria-label="Office sign outside the practice"></div>
<div class="rule-band" style="top:2616px;height:2px;background:linear-gradient(90deg,var(--teal),var(--purple))"></div>

<!-- team -->
<h2 class="section-title" style="top:2661px">Our Team</h2>
<div class="title-divider" style="top:2714px"><svg width="20" height="20" viewBox="0 0 20 20"><path d="M4 3h12v8c0 4-3 6-6 7-3-1-6-3-6-7z" fill="none" stroke="var(--teal)" stroke-width="2"/><path d="M7 7h6v3c0 2-1.5 3-3 3.5C8.5 13 7 12 7 10z" fill="var(--purple)"/></svg></div>
<svg class="slider-arrow" style="left:30px" width="20" height="36" viewBox="0 0 20 36"><path d="M16 4L4 18l12 14" fill="none" stroke="#8a8e96" stroke-width="3"/></svg>
<svg class="slider-arrow" style="left:1150px" width="20" height="36" viewBox="0 0 20 36"><path d="M4 4l12 14L4 32" fill="none" stroke="#8a8e96" stroke-width="3"/></svg>
<div class="team-card" style="left:100px"><div class="team-photo" role="img" aria-label="Portrait of Dr. Meera Kalwani"><div class="team-caption"><span class="name">Dr. Meera Kalwani</span><span class="role">Dental surgeon</span></div></div></div>
<div class="team-card" style="left:345px"><div class="team-photo" role="img" aria-label="Portrait of Dr. Hannah Corwin"><div class="team-caption"><span class="name">Dr. Hannah Corwin</span><span class="role">Dental surgeon</span></div></div></div>
<div class="team-card" style="left:590px"><div class="team-photo" role="img" aria-label="Portrait of Dr. Anika Sorel"><div class="team-caption"><span class="name">Dr. Anika Sorel</span><span class="role">Dental surgeon</span></div></div></div>
<div class="team-card" style="left:880px"><div class="team-photo" role="img" aria-label="Portrait of Dena Marlow"><div class="team-caption"><span class="name">Dena Marlow</span><span class="role">Dental surgeon</span></div></div></div>
<div class="rule-band" style="top:3112px;height:2px;background:linear-gradient(90deg,var(--teal),var(--purple))"></div>

<!-- testimonials -->
<h2 class="section-title" style="top:3158px">Our Patient's Testimonial</h2>
<div class="title-divider" style="top:3211px"><svg width="20" height="20" viewBox="0 0 20 20"><path d="M4 3h12v8c0 4-3 6-6 7-3-1-6-3-6-7z" fill="none" stroke="var(--teal)" stroke-width="2"/><path d="M7 7h6v3c0 2-1.5 3-3 3.5C8.5 13 7 12 7 10z" fill="var(--purple)"/></svg></div>
<div class="testimonial" style="left:79px">
  <span class="quote-mark">“</span>
  <p>Friendly staff, gentle care and a calm office. I no longer dread my checkups and my whole family now comes here for cleanings and fillings.</p>
  <span class="author">Tom Avery<small>Patient</small></span>
  <div class="avatar" role="img" aria-label="Patient portrait"></div>
</div>
<div class="testimonial" style="left:613px">
  <span class="quote-mark">“</span>
  <p>The team explained every step and made my crown visit painless. Scheduling was easy and the results look great. Highly recommended to anyone nervous.</p>
  <span class="author">Clara Benning<small>Patient</small></span>
  <div class="avatar" role="img" aria-label="Patient portrait"></div>
</div>
<div class="rule-band" style="top:3527px;height:3px;background:linear-gradient(90deg,var(--purple),var(--teal))"></div>

<!-- contact -->
<section class="contact"></section>
<h2 class="section-title" style="top:3573px">Contact Us</h2>
<div class="title-divider" style="top:3626px"><svg width="20" height="20" viewBox="0 0 20 20"><path d="M4 3h12v8c0 4-3 6-6 7-3-1-6-3-6-7z" fill="none" stroke="var(--teal)" stroke-width="2"/><path d="M7 7h6v3c0 2-1.5 3-3 3.5C8.5 13 7 12 7 10z" fill="var(--purple)"/></svg></div>
<div class="contact-info">
  <span class="label">Call us for any information :</span>
  <span class="phone">555-014-2230/2231</span>
  <span class="label">Contact with us :</span>
  <span>418 E. Linden Ave, Suite 2C<br>Maplecrest, OH 45001</span>
  <span class="label">Contact us for your Estimation :</span>
  <span class="hi">info@grinsofmaplecrest.example</span>
  <span class="hi">www.grinsofmaplecrest.example</span>
  <span class="label">Opening Hours :</span>
  <div class="hours">
    <div><span>Monday:</span> 12:00pm to 6:00pm</div>
    <div><span>Tuesday:</span> 10:00am to 7:00pm</div>
    <div><span>Wednesday:</span> Closed</div>
    <div><span>Thursday:</span> 8:00am to 6:00pm</div>
    <div><span>Friday:</span> 8:00am to 5:00pm</div>
    <div><span>Saturday when open:</span> 8:00am to 3:00pm OR 8:00am to 12:00pm</div>
  </div>
</div>
<div class="form-divider"></div>
<div class="contact-form">
  <label style="top:3728px">Name :</label><div class="field" style="top:3716px">Enter your Name</div>
  <label style="top:3793px">Email :</label><div class="field" style="top:3781px">Enter your Email Address</div>
  <label style="top:3858px">Phone :</label><div class="field" style="top:3846px">Enter your Phone Number</div>
  <label style="top:3926px">Address :</label><div class="field" style="top:3914px">Enter your Address</div>
  <label style="top:3999px">Message :</label><div class="field" style="top:3987px;height:72px">Enter your Message</div>
  <div class="send-btn">Send</div>
</div>

<footer class="site-footer">
  <div class="footer-nav"><span>Home</span><span class="sep">|</span><span>About</span><span class="sep">|</span><span>Services</span><span class="sep">|</span><span>Patient Education</span><span class="sep">|</span><span>Patient Form</span><span class="sep">|</span><span>Testimonial</span><span class="sep">|</span><span>Contact</span></div>
  <div class="copyright">© 2016 info@grinsofmaplecrest.example . All rights reserved</div>
  <div class="legal"><span>Terms &amp; Conditions</span><span>|</span><span>Privacy Policy</span></div>
  <div class="social-square" aria-label="Friendwall"></div>
</footer>

</body>
</html>
```